Harbinger Noble Alloys Works Business Cards

We are wanting to have a new business card designed for our company as we go to a convention. We want to balance business/Modern with elegance and beauty. Our company sells highend jewelry pieces. We want to utilize the colors of Black and Gold and have gold foiled fonts to be physically printed on the business cards.
We also would like to have space to write notes on the back side of the business card. When we meet people at jewelry conventions we would like to write notes if possible.
Here are websites and designs that we like the look and feel of these companies and you can use these as design ideas.
https://www.lorvanne.com
https://www.bellquist.com/en-us/home
Here is our company website link
www.harbingernaw.com
I also up loaded two versions of our logo.
- Update 4.26.22
I have uploaded photos of a business card we like. this card has raised embossed letters that you can feel. the raise letters are like a plastic but we don't need to use that...I uploaded to show you that we like the experience of the client feeling the characters of the logo. we also would like to have the material as a satin or some material very soft.
- Maybe we can get designs with beautiful gold foiling and raised characters and logos. we like simplicity...not busy but an elegant design. We need to write notes and would like a section where we can write notes. but we want an elegant style and the client has an experience with the feel of the card when they touch the card.
Colors
- Main colors Black & Gold
- white or light colors for small notes section.
Specialty ideals and things we would like to see based on your design styles.
- raised fonts
- raised logos
- gold foiling
- satin/soft finish on the card material.
we are wanting to design a business card that looks elegant and clean. When the client is handed the business card we want them to physically experience the business card as well by touching the raised logos or fonts and the base material is soft satin. I hope this helps with further designs.
thank you all
We uploaded a new contact layout that we have designed in our office. we would like to see how this would look on your designs.
thank you
I just finished uploading the Contact Layout. the colors are just examples. please use this layout as an idea and use colors based on the feed back we have given each of you personally.
Contact Information for Business Card
we need an area to write notes, we would like to have our logos or the diamond of our logo or the business card to have embossed sections to the business card so when the customer touches the card they can feel the logo. we would also like sections of our business card to have gold foiling. we would also like to use a satin soft paper with our card. when the client touches the card its super soft and high quality
Requirements
Must have
- we would like to have our logos or the diamond of our logo or the business card to have embossed sections to the business card so when the customer touches the card they can feel the logo. we would also like sections of our business card to have gold foiling. we would also like to use a satin soft paper with our card. when the client touches the card its super soft and high quality
Nice to have
- we would like to have our logos or the diamond of our logo or the business card to have embossed sections to the business card so when the customer touches the card they can feel the logo. we would also like sections of our business card to have gold foiling.

```html
<!DOCTYPE html>
<html lang="en">
<head>
<meta charset="utf-8">
<title>Harbinger Noble Alloys – Business Card</title>
<link rel="stylesheet" href="https://fonts.googleapis.com/css2?family=Cinzel:wght@500&family=Montserrat:ital,wght@0,300;0,700;1,700&display=swap">
<style>
  :root {
    --card-black: #000000;
    --page-white: #ffffff;
    --foil-gold: #878a1e;
    --foil-gold-soft: #8d9024;
  }
  html, body {
    margin: 0;
    padding: 0;
    width: 1200px;
    height: 686px;
    overflow: hidden;
    background: var(--page-white);
  }
  .card {
    position: relative;
    width: 1200px;
    height: 686px;
  }
  .card-shape {
    position: absolute;
    inset: 0;
  }
  .brand {
    position: absolute;
    left: 0;
    right: 0;
    text-align: center;
    color: var(--foil-gold);
  }
  .brand-name {
    top: 158px;
    font-family: "Cinzel", serif;
    font-weight: 500;
    font-size: 58px;
    line-height: 64px;
    letter-spacing: 0.5px;
    margin: 0;
  }
  .brand-tagline {
    top: 226px;
    font-family: "Cinzel", serif;
    font-weight: 500;
    font-size: 40px;
    line-height: 48px;
    letter-spacing: 0.5px;
    margin: 0;
  }
  .contact {
    position: absolute;
    left: 0;
    right: 0;
    top: 315px;
    margin: 0;
    text-align: center;
    font-family: "Montserrat", sans-serif;
    font-style: normal;
    font-weight: 300;
    font-size: 30px;
    line-height: 40px;
    color: var(--foil-gold-soft);
  }
  .contact-name {
    display: block;
    font-weight: 700;
  }
  .contact-title {
    display: block;
    font-weight: 700;
    font-style: italic;
  }
  .contact-line {
    display: block;
  }
</style>
</head>
<body>
  <main class="card">
    <svg class="card-shape" width="1200" height="686" viewBox="0 0 1200 686" aria-hidden="true">
      <polygon points="51,0 1149,0 1200,51 1200,635 1149,686 51,686 0,635 0,51" fill="var(--card-black)"/>
      <polygon points="149,59 1049,59 1118,126 1118,560 1049,624 149,624 82,560 82,126"
               fill="none" stroke="var(--foil-gold)" stroke-width="3.5"/>
    </svg>

    <h1 class="brand brand-name">Harbinger Noble Alloys</h1>
    <p class="brand brand-tagline">– Coins, &nbsp;Jewelry &amp; Diamonds –</p>

    <address class="contact">
      <span class="contact-name">Employee name</span>
      <span class="contact-title">title/position</span>
      <span class="contact-line">2740 Larkmoor Ave NE</span>
      <span class="contact-line">Fenwick, OR 97388</span>
      <span class="contact-line">Phone: (503) 555-0174</span>
      <span class="contact-line">test@harbingernaw.com</span>
      <span class="contact-line">www.harbingernaw.com</span>
    </address>
  </main>
</body>
</html>
```